WELL DRILLING COMPANY NEEDS A THANK YOU POSTCARD

We need a postcard that expresses a "thank you for choosing us to drill your water well" and also expresses and appreciation for any referrals sent our way. We drill domestic and agricultural water wells. We would like to see designs that uses the colors red and light brown (tan). On the back of the postcard we are telling our customers that we also provide septic services including septic pumping maintenance

Target Market(s)

Our past customers whom we have drilled a water well for but may not know that we also do septic installations including septic tank pumping.

Industry/Entity Type

It Company

Font styles to use
Sans Serif

Colors
ec1f27
f8ba93

Requirements
Must have
• The front of the postcard should be the red and tan business card sign, with a small picture of the drill rig on the bottom left side and the other picture of the 3 men on the bottom right side. Incorporate a thank you for choosing us to drill your well toward the bottom of the card. Basically the front of the postcard is thanking our past customers for using us to dril their water well and the back of the postcard is to promote our septic installation / septic tank pumping business.
Nice to have
• Use Red & Tan colors. "thank you" working for using us to drill their water well.
• On the Back of the Postcard, wording to introduce them to our other company "Marlowe Pumping" where we also install septic systems and perform septic pumping services.

```html
<!DOCTYPE html>
<html lang="en">
<head>
<meta charset="utf-8">
<title>Thank You Postcard – Front and Back</title>
<link rel="stylesheet" href="https://fonts.googleapis.com/css2?family=Roboto+Condensed:wght@700&family=Lato:wght@400&display=swap">
<style>
  :root {
    --red: #ec1f27;
    --tan: #f8ba93;
    --white: #ffffff;
    --ink: #444444;
    --stamp: #808080;
    --page: #ffffff;
  }
  html, body {
    margin: 0;
    padding: 0;
    width: 1200px;
    height: 1200px;
    overflow: hidden;
    background: var(--page);
  }
  .sheet {
    position: relative;
    width: 1200px;
    height: 1200px;
  }
  .postcard {
    position: absolute;
    left: 260px;
    width: 644px;
    height: 500px;
    box-shadow: 3px 4px 6px rgba(0,0,0,0.35);
    background: var(--white);
  }
  .postcard--front { top: 54px; }
  .postcard--back { top: 612px; }
  .postcard svg { display: block; width: 644px; height: 500px; }

  .headline {
    font-family: "Roboto Condensed", "Arial Narrow", sans-serif;
    font-weight: 700;
  }
  .headline--main { fill: var(--red); font-size: 64px; }
  .headline--sub { fill: var(--tan); font-size: 43px; }
  .thanks { fill: var(--white); font-size: 27px; }
  .brand-name { fill: var(--white); font-size: 40px; }
  .call-label { fill: var(--white); font-size: 31px; }
  .service {
    font-family: "Lato", Arial, sans-serif;
    font-size: 19px;
    fill: var(--ink);
  }
  .service-dot { fill: var(--red); }
  .phone {
    font-family: "Lato", Arial, sans-serif;
    font-size: 20px;
    fill: var(--white);
  }
</style>
</head>
<body>
<main class="sheet">

  <!-- Front of postcard -->
  <section class="postcard postcard--front" aria-label="Postcard front">
    <svg viewBox="0 0 805 625" xmlns="http://www.w3.org/2000/svg">
      <defs>
        <linearGradient id="faintWorkshop" x1="0" y1="0" x2="1" y2="1">
          <stop offset="0" stop-color="#f4f4f4"/>
          <stop offset="0.5" stop-color="#ececec"/>
          <stop offset="1" stop-color="#f6f6f6"/>
        </linearGradient>
        <linearGradient id="sunsetRig" x1="0" y1="0" x2="0" y2="1">
          <stop offset="0" stop-color="#6a5a86"/>
          <stop offset="0.5" stop-color="#c36a5a"/>
          <stop offset="1" stop-color="#3b3550"/>
        </linearGradient>
        <linearGradient id="crewTruck" x1="0" y1="0" x2="1" y2="1">
          <stop offset="0" stop-color="#b9b4a6"/>
          <stop offset="0.6" stop-color="#8c8576"/>
          <stop offset="1" stop-color="#4d4a44"/>
        </linearGradient>
      </defs>

      <rect class="front-backdrop" x="0" y="0" width="805" height="400" fill="url(#faintWorkshop)" role="img" aria-label="Faint background photo of well pump equipment"/>
      <rect x="0" y="400" width="805" height="225" fill="var(--white)"/>

      <text class="headline headline--main" x="410" y="202" text-anchor="middle">WE DRILL DOMESTIC AND</text>
      <text class="headline headline--sub" x="410" y="252" text-anchor="middle">AGRICULTURAL WATER WELLS</text>

      <!-- tan frames -->
      <polygon points="0,397 194,397 348,625 0,625" fill="var(--tan)"/>
      <polygon points="616,397 805,397 805,625 466,625" fill="var(--tan)"/>

      <!-- photos -->
      <polygon points="0,404 188,404 338,625 0,625" fill="url(#sunsetRig)" role="img" aria-label="Photo of a drill rig against a sunset sky"/>
      <polygon points="622,404 805,404 805,625 477,625" fill="url(#crewTruck)" role="img" aria-label="Photo of three crew members standing by a drilling truck"/>

      <!-- red message panel -->
      <polygon points="212,420 605,420 488,592 330,592" fill="var(--red)"/>
      <text class="headline thanks" x="406" y="478" text-anchor="middle">THANK YOU FOR</text>
      <text class="headline thanks" x="406" y="509" text-anchor="middle">CHOOSING US TO DRILL</text>
      <text class="headline thanks" x="406" y="540" text-anchor="middle">YOUR WATER WELL</text>
    </svg>
  </section>

  <!-- Back of postcard -->
  <section class="postcard postcard--back" aria-label="Postcard back">
    <svg viewBox="0 0 805 625" xmlns="http://www.w3.org/2000/svg">
      <defs>
        <linearGradient id="plumberPhoto" x1="0" y1="0" x2="0" y2="1">
          <stop offset="0" stop-color="#8d8f96"/>
          <stop offset="0.6" stop-color="#c9cacf"/>
          <stop offset="1" stop-color="#f2f2f2"/>
        </linearGradient>
      </defs>

      <polygon points="0,0 414,0 381,225 0,225" fill="url(#plumberPhoto)" role="img" aria-label="Photo of a technician working on pipes with a red wrench"/>

      <!-- slanted accent stripes -->
      <polygon points="418,0 426,0 351,515 343,515" fill="var(--red)"/>
      <polygon points="428,0 433,0 358,515 353,515" fill="var(--tan)"/>

      <rect x="0" y="225" width="372" height="90" fill="var(--tan)"/>
      <text class="headline brand-name" x="24" y="284">MARLOWE PUMPING</text>

      <circle class="service-dot" cx="24" cy="344" r="2.6"/>
      <text class="service" x="30" y="350">septic installation</text>
      <circle class="service-dot" cx="24" cy="369" r="2.6"/>
      <text class="service" x="30" y="375">septic tank pumping business.</text>

      <polygon points="0,425 357,425 343,515 0,515" fill="var(--red)"/>
      <text class="headline call-label" x="20" y="480">Call now</text>
      <text class="phone" x="153" y="477">09876543210</text>

      <rect class="stamp-box" x="701" y="15" width="87" height="104" fill="var(--stamp)"/>
    </svg>
  </section>

</main>
</body>
</html>
```